Business card design needed for Pebble Bakes

We need a new business card designed for our business. We create complete DIY cake kits to be delivered Australia Wide.

I would like our logo used (see attached).

Industry/Entity Type

Business

Contact Information for Business Card

Pebble Bakes - Complete DIY Cake Kits
www.pebblebakes-demo.com.au
0400 152 947
sales@pebblebakes-demo.com.au
www.facebook.com/pebblebakes7

Requirements
Must have
• logo

```html
<!DOCTYPE html>
<html lang="en">
<head>
<meta charset="utf-8">
<title>Pebble Bakes – Business Card</title>
<link rel="stylesheet" href="https://fonts.googleapis.com/css2?family=Fredoka:wght@600;700&family=Questrial&display=swap">
<style>
  :root {
    --page: #ffffff;
    --card-top: #df6aa7;
    --card-bottom: #e77fb5;
    --ribbon: #e1368b;
    --ribbon-shadow: #b8236c;
    --white: #ffffff;
    --outline: #474747;
    --ink-grey: #4a4a4a;
    --art-hair: #9a6a3e;
    --art-skin: #f6d3b4;
    --art-pink: #f19ac4;
    --art-red: #c8303f;
  }
  html, body {
    margin: 0;
    padding: 0;
    width: 1200px;
    height: 693px;
    overflow: hidden;
    background: var(--page);
  }
  .canvas {
    position: relative;
    width: 1200px;
    height: 693px;
  }
  .card {
    position: absolute;
    left: 46px;
    top: 46px;
    width: 1104px;
    height: 600px;
    border-radius: 12px;
    overflow: hidden;
    background: var(--card-top);
  }
  .card-bands {
    position: absolute;
    inset: 0;
  }
  .brand-title {
    position: absolute;
    left: 60px;
    top: 150px;
    margin: 0;
    font-family: "Fredoka", sans-serif;
    font-weight: 700;
    font-size: 84px;
    letter-spacing: 1px;
    color: var(--white);
    -webkit-text-stroke: 12px var(--outline);
    paint-order: stroke fill;
    text-shadow: 3px 5px 6px rgba(0,0,0,0.35);
    transform: rotate(-3deg);
    transform-origin: left center;
    white-space: nowrap;
  }
  .tagline {
    position: absolute;
    left: 76px;
    top: 250px;
    width: 572px;
    height: 52px;
    border-radius: 26px;
    background: var(--ribbon);
    box-shadow: 0 6px 0 var(--ribbon-shadow), 2px 8px 10px rgba(0,0,0,0.25);
    transform: rotate(-3deg);
    transform-origin: left center;
    display: flex;
    align-items: center;
    justify-content: center;
    font-family: "Fredoka", sans-serif;
    font-weight: 600;
    font-style: italic;
    font-size: 36px;
    letter-spacing: 1px;
    color: var(--white);
    white-space: nowrap;
  }
  .contact {
    position: absolute;
    left: 110px;
    top: 338px;
    width: 540px;
    margin: 0;
    list-style: none;
    padding: 0;
    text-align: center;
    font-family: "Questrial", sans-serif;
    font-size: 33px;
    line-height: 45px;
    color: var(--white);
    transform: rotate(-3deg);
    text-shadow: 1px 2px 3px rgba(0,0,0,0.15);
  }
  .social {
    position: absolute;
    left: 12px;
    bottom: 12px;
    display: flex;
    align-items: center;
    gap: 6px;
    font-family: "Questrial", sans-serif;
    font-size: 24px;
    color: var(--ink-grey);
  }
  .social-square {
    width: 32px;
    height: 32px;
    border-radius: 4px;
    background: var(--ink-grey);
  }
  .mascot-art {
    position: absolute;
    left: 650px;
    top: 28px;
    width: 440px;
    height: 410px;
    border-radius: 46% 46% 28% 28%;
    background: radial-gradient(ellipse at 62% 30%, var(--art-skin) 0%, var(--art-pink) 45%, var(--art-hair) 80%, var(--art-red) 100%);
    opacity: 0.9;
  }
  .logo-name {
    position: absolute;
    left: 640px;
    top: 470px;
    width: 460px;
    margin: 0;
    text-align: center;
    font-family: "Questrial", sans-serif;
    font-size: 48px;
    line-height: 60px;
    color: var(--white);
    white-space: nowrap;
  }
</style>
</head>
<body>
<div class="canvas">
  <section class="card">
    <svg class="card-bands" width="1104" height="600" viewBox="0 0 1104 600" aria-hidden="true">
      <rect width="1104" height="600" fill="var(--card-top)"/>
      <polygon points="0,348 1104,293 1104,600 0,600" fill="var(--card-bottom)"/>
    </svg>

    <h1 class="brand-title">Pebble Bakes</h1>
    <div class="tagline">Complete DIY Cake Kits</div>

    <ul class="contact">
      <li class="contact-web">www.pebblebakes-demo.com.au</li>
      <li class="contact-phone">0400 152 947</li>
      <li class="contact-email">sales@pebblebakes-demo.com.au</li>
    </ul>

    <div class="social">
      <span class="social-square"></span>
      <span class="social-handle">fb.com/pebblebakes7</span>
    </div>

    <div class="mascot-art" role="img" aria-label="Illustration of a smiling baker piping pink icing onto a cupcake"></div>
    <p class="logo-name">Pebble Bakes</p>
  </section>
</div>
</body>
</html>
```